White Paper and One-Page Advertisement for TELVAMORE-QX

I need both documents to be better formatted and designed so they look professional, not something someone with mediocre word skills put together. They will go out to 1000s of industry professionals, and they need to look sharp. I need them to have my company's color palate logo, and branding on it similar to how it is now, but better. Please do not change any of the written content, but it can be arranged in any other format you think is better. Smart art and things i've already used can be omitted in favor of better designs. The developer is free to use their creativity. White paper should not be longer than the three pages unless necessary.

Target Market(s)

Life Sciences supply chain professionals

Colors
33b8a4
0592cd
9bcb3c
fbee3e
3277b5

Requirements
Must have
• Must be professional looking and not look like something done in word. Please use the color palate as seen on the documents.
Should not have
• Any changes to the written content.

```html
<!DOCTYPE html>
<html lang="en">
<head>
<meta charset="utf-8">
<title>White Paper – Page 2</title>
<link href="https://fonts.googleapis.com/css2?family=Barlow+Condensed:wght@500;600&family=Barlow:ital,wght@0,400;0,600;1,500&display=swap" rel="stylesheet">
<style>
:root{
  --bg:#dde8c6;
  --paper:#ffffff;
  --ink:#2a2a2a;
  --green:#7db443;
  --lime:#c6d94b;
  --forest:#2f8a6c;
  --teal:#6cb1b4;
  --tint-green:#e7efd4;
  --tint-lime:#f2f5d8;
  --tint-forest:#dbe6dc;
  --tint-teal:#dcecec;
  --rule:#4a9a86;
  --faint:#eef2e6;
}
*{margin:0;padding:0;box-sizing:border-box}
html,body{width:838px;height:1200px;overflow:hidden}
body{background:var(--bg);font-family:"Barlow",sans-serif;color:var(--ink);position:relative}
.page-label{position:absolute;left:64px;top:36px;font:600 14px "Barlow",sans-serif;letter-spacing:.3px}
.side-strip{position:absolute;left:38px;top:78px;width:30px;height:1074px;background:linear-gradient(#cadd90,#4e8a70)}
.sheet{position:absolute;left:68px;top:78px;width:730px;height:1074px;background:var(--paper)}
.backdrop-circle{position:absolute;left:580px;top:100px;width:200px;height:200px;border-radius:50%;border:14px solid var(--faint)}
.col{position:absolute;font-size:9.5px;line-height:13px}
.left{left:96px;width:323px}
.right{left:446px;width:324px}
p{text-align:justify}
h2{font:600 19px/22px "Barlow Condensed",sans-serif;color:#1e1e1e}
h3{font:600 14px/17px "Barlow Condensed",sans-serif;color:#1e1e1e}
h4{font:600 9.8px/13px "Barlow",sans-serif}
.sub{font:italic 500 10.5px/13px "Barlow",sans-serif;color:var(--green)}
ul{list-style:none}
li{position:relative;padding-left:10px}
li::before{content:"";position:absolute;left:1px;top:5px;width:4px;height:4px;border-radius:50%;background:var(--green)}
.stats{display:grid;grid-template-columns:repeat(4,81px);position:absolute;left:96px;top:138px}
.stat-head{height:25px;display:flex;align-items:center;justify-content:center;color:#fff;font:600 16px "Barlow Condensed",sans-serif}
.stat-body{height:77px;padding:5px 8px;text-align:center;font-size:9px;line-height:12.3px}
.callout{border-left:3px solid var(--rule);padding-left:8px;margin-bottom:11px;font-size:11.5px;line-height:15px}
.callout b{font:600 19px "Barlow Condensed",sans-serif;color:var(--green);margin-right:4px}
.callout ul{margin:8px 0 0 22px}
.bullwhip{position:absolute;left:446px;top:678px;width:324px;height:53px;display:grid;grid-template-columns:1fr 1fr;grid-template-rows:1fr 1fr}
.bullwhip div{color:#fff;font:600 11.5px "Barlow Condensed",sans-serif;display:flex;align-items:center;padding:0 10px}
.bullwhip .center{position:absolute;left:108px;top:15px;width:108px;height:23px;background:#fff;color:#1e1e1e;justify-content:center;font-size:11px}
.page-num{position:absolute;left:758px;top:1118px;border-left:2px solid var(--green);padding-left:5px;font:600 10px "Barlow",sans-serif;height:14px}
</style>
</head>
<body>
<div class="page-label">PAGE 2</div>
<div class="side-strip"></div>
<div class="sheet"></div>
<div class="backdrop-circle" aria-hidden="true"></div>

<div class="stats">
  <div class="stat-head" style="background:var(--green)">3.77%</div>
  <div class="stat-head" style="background:var(--lime)">$2.7B</div>
  <div class="stat-head" style="background:var(--forest)">.01</div>
  <div class="stat-head" style="background:var(--teal)">$2,034</div>
  <div class="stat-body" style="background:var(--tint-green)">Avg Raw Material Write-down as a % of Net Income</div>
  <div class="stat-body" style="background:var(--tint-lime)">Est Pharma Written Down Inventory in 2016</div>
  <div class="stat-body" style="background:var(--tint-forest)">Est US Pharma Revenue per 1 Ton Non-MSW Waste</div>
  <div class="stat-body" style="background:var(--tint-teal)">Correlation Coefficent of Material Write-downs and Firm Size</div>
</div>

<div class="col left" style="top:258px">
  <h2 style="margin-bottom:8px">What Do These Numbers Mean?</h2>
  <div class="callout"><b>3.77%</b> is an alarmingly high, and does not include capitalized consumables, equipment disposal, and similar wastes
    <ul><li>$5B in net income LS Firm: est $185M in write-downs</li><li>$50M in net income LS Firm: est $1.9M in write-downs</li></ul>
  </div>
  <div class="callout"><b>$2.7B</b> is likely much lower than the real figure due to capitalizing consumable inventories for launches etc.</div>
  <div class="callout"><b>.01</b> correlation coefficient means this problem does not discriminate based on company size and is ubiquitous in the industry.</div>
  <div class="callout" style="border-left-color:var(--teal)"><b style="color:var(--teal)">$2,034</b> to one ton of industrial waste is not progressive.</div>
</div>

<div class="col left" style="top:534px">
  <p style="margin-bottom:13px">Industries have attempted to mitigate the bullwhip effect through many techniques and systems such as ERP, robust forecasting models, demand management, LSS tools, strategic sourcing, etc. However, life science firms still struggle to effectively address this problem as evidenced by the write-down figures.</p>
  <p style="margin-bottom:13px">Many non-FDA regulated industries have started utilizing marketplaces and brokerage services to create circular supply chains that optimize waste by connecting buyers and sellers. However, Pharma and life sciences have yet to adopt this <b>waste-centric supply chain</b> and execute it in a manner conducive to the compliance and indemnification requirements of the industry regarding primary and secondary transactions of raw materials, equipment, consumables, spare parts, and collaborative relationships. Finished products such as APIs, intermediates, and devices are out of scope for this supply chain.</p>
  <p style="margin-bottom:13px"><b>A life sciences marketplace and consortium</b> for manufacturers, reserachers, and vendors can minimize the aforementioned problems by quickly, innovatively, and transparently exchanging material information in safe and controlled environment ensuring a firm's standards for data integrity, cGMP compliance, contractual indemnification, and financial benefits are met; all by leveraging core auditing skills.</p>
  <p style="margin-bottom:13px">It is a call to arms among supply chain, procurement, and quality leaders to take part in a more circular, greener, and collaborative supply chain. Time is critical as global competition grows, customer and government emphasis on lowering pricing mounts5, and collective pressure on sustainability demands widespread action.</p>
  <p>Let's explore <b>Current</b> and <b>Future State</b> of this industry issue to understand why such a marketplace can begin the much-needed transition for life science companies.</p>
</div>

<div class="col left" style="top:958px">
  <h2>Baseline Problem</h2>
  <h3>What?</h3>
  <ul style="margin-left:22px">
    <li>Disposal of high quality materials, equipment, spare parts</li>
    <li>Single and/or limited sources of supply</li>
    <li>Inability to collaborative with like-minded life sciences firms</li>
    <li>High CoGS due to materials write-downs</li>
    <li>High inventory carrying costs</li>
    <li>Greater business continuity risk</li>
    <li>High disposal costs</li>
    <li>Larger environmental footprint</li>
    <li>Stock-out of materials</li>
  </ul>
</div>

<div class="col right" style="top:134px">
  <h3>Who?</h3>
  <ul style="margin-left:22px;margin-bottom:16px"><li>FDA Regulated Industries, Procurement, Quality, Production, and Finance.</li></ul>
  <h3>Where &amp; When</h3>
  <ul style="margin-left:22px;margin-bottom:16px"><li>Commercial &amp; clinical production, R&amp;D, sourcing/purchasing, production planning, quality testing, etc.</li><li>Volatile demand periods, e.g., product intro growth, decline, seasonality, economic uncertainty, and unforeseen events.</li></ul>
  <h3>How do we know it's there?</h3>
  <ul style="margin-left:22px;margin-bottom:18px"><li>We physically see it taking place, and it's in our data.</li></ul>
  <h3>Triple Bottom Line Impact</h3>
  <div class="sub">Financial</div>
  <div style="margin-left:33px;margin-top:3px"><h4>Vendors/ Sellers</h4></div>
  <ul style="margin-left:22px;margin-bottom:6px"><li>Higher write-downs/offs and 3rd party disposal fees</li></ul>
  <div style="margin-left:33px"><h4>Buyers</h4></div>
  <ul style="margin-left:22px;margin-bottom:7px"><li>Lost sales – stock-outs</li><li>Inflated market value of materials &amp; supplier expedition fees</li><li>High SS cost due to bullwhip effect</li></ul>
  <div class="sub">Environment</div>
  <ul style="margin-left:22px;margin-bottom:9px"><li>Greater contribution to global warming through landfill addition, incineration, inactivation, and energy consumption.</li><li>Noncompliance with ISO 14000 &amp; 9000 and B-Corp Status</li></ul>
  <div class="sub">Society</div>
  <ul style="margin-left:22px;margin-bottom:20px"><li>Lost community trust - high environment and consumer costs</li><li>Less Innovation, collaboration, and supply chain optimization</li></ul>
  <h3>Current State</h3>
  <div class="sub">External Solutions</div>
  <p>Pharma and other FDA industries spend considerable energy on reducing waste. A plethora of techniques are employed to mitigate, prepare for, respond to, and recover from the bullwhip effect, which is one of the leading causes of write-downs and waste. However, such efforts are predicated on:</p>
</div>

<div class="bullwhip">
  <div style="background:var(--green)">Forecast Accuracy</div>
  <div style="background:var(--lime);justify-content:flex-end">Supplier Reliability</div>
  <div style="background:var(--forest)">Process Variability</div>
  <div style="background:var(--teal);justify-content:flex-end">External Environment</div>
  <div class="center">Bullwhip Influences</div>
</div>

<div class="col right" style="top:747px">
  <p style="margin-bottom:13px">While not fruitless, attempts to mitigate the above external influences are extremely unpredictable and have never solved pharma's write-down, inefficiency, stock-out, and environmental problems.</p>
  <h4>Internal Solutions</h4>
  <p style="margin-bottom:13px">The next effort involves reducing obsolescence by making use of materials within the firm. Typically, interplant demand is the only outlet to optimize surplus earmarked for a reserve/write-down. Even this involves many of the same regulatory compliance, quality, and economic challenges. Facilitating this takes time, resources, and does not provide a broad network to utilize.</p>
  <h4>Environmental Solutions</h4>
  <p style="margin-bottom:13px">FDA industries, like most others, make attempts to reuse, recycle, and convert to energy where applicable. However, they're unable to conduct these activities for perishable, expiring, and/or consumable materials.</p>
  <h4>Undesirable Solutions</h4>
  <p style="margin-bottom:13px">Unfortunately, third party disposal (frequently landfill) is typically the first and most popular option as perishable, expiring, and complex materials are generally unable to be reused or recycled. These disposals come in many forms to include responsible landfills, incineration, inactivation, etc.</p>
  <h4>Overall</h4>
  <p>Industries spend much capital and resources to reduce write-downs in an environment where the bullwhip effect reigns supreme. Mitigations to this effect are attempted but only partially successful or sustainable.</p>
</div>

<div class="page-num">1</div>
</body>
</html>
```